Desing for real estate offers- Package system

The word should be graphically clear and understandable. There are 3 packages that the customer can buy: the basic package is red, the medicinal package is green and the carefree package is blue. See the Word document in the appendix. End file should be a Word, as we need to chance the text. It should also match the website as well as the business card.
https://brelvona.domistra.ch/
Colors:
Green 1: R: 187, G: 214, B: 49
Green 2: R: 119, G: 187, W: 66

Target Market(s)

Real estate company

Font styles to use
Serif
Sans Serif

```html
<!DOCTYPE html>
<html lang="de">
<head>
<meta charset="utf-8">
<title>Brelvona – Verkaufspakete</title>
<link href="https://fonts.googleapis.com/css2?family=Arimo:wght@400;700&display=swap" rel="stylesheet">
<style>
  :root{
    --green-1:#bbd631;
    --green-2:#77bb42;
    --brand-green:#8cc63f;
    --red-top:#e8101c;
    --red-bottom:#b8000a;
    --blue-top:#35a8ea;
    --blue-bottom:#1a86cc;
    --text:#2b2b2b;
    --muted:#8a8a8a;
    --row-alt:#f0f0f0;
    --price-bg:#e9e9e9;
  }
  *{margin:0;padding:0;box-sizing:border-box}
  html,body{width:1200px;height:844px;overflow:hidden;background:#fff}
  body{position:relative;font-family:"Arimo",Arial,sans-serif;color:var(--text)}

  .top-band{position:absolute;left:0;top:0;width:1200px;height:6px;
    background:linear-gradient(90deg,var(--green-1),var(--green-2))}

  .brand{position:absolute;left:102px;top:62px;font-size:62px;font-weight:700;
    color:var(--brand-green);letter-spacing:-0.5px;line-height:1}
  .header-divider{position:absolute;left:473px;top:55px;width:1px;height:100px;background:#b9d98a}
  .notice{position:absolute;left:500px;top:84px;font-size:18.5px;line-height:1.5;color:var(--muted);white-space:nowrap}

  .packages{position:absolute;left:101px;top:194px;width:1010px;border-collapse:separate;border-spacing:0;table-layout:fixed}
  .packages col.task{width:392px}
  .packages col.basis{width:190px}
  .packages col.medium{width:188px}
  .packages col.sorglos{width:240px}

  .package-head th{height:68px;color:#fff;font-weight:400;font-size:20px;border-radius:7px 7px 0 0;border-left:3px solid #fff}
  .package-head th.blank{background:none;border:none}
  .package-head .basis{background:linear-gradient(var(--red-top),var(--red-bottom))}
  .package-head .medium{background:linear-gradient(var(--blue-top),var(--blue-bottom))}
  .package-head .sorglos{background:linear-gradient(var(--green-1),var(--green-2))}

  .price-row td{height:67px;background:var(--price-bg);text-align:center;font-weight:700;font-size:12.5px;
    color:#555;line-height:1.35;padding:0 8px;border-left:3px solid #fff;border-top:3px solid #fff}
  .price-row td.price-note{font-size:11.5px;padding:0 2px;white-space:nowrap}
  .price-row td.section-title{background:none;border:none;text-align:left;padding-left:10px;
    font-size:22px;font-weight:400;color:var(--green-2);vertical-align:top;padding-top:2px}

  .steps td{height:17.6px;font-size:10.5px;line-height:17.6px;padding-left:10px;white-space:nowrap}
  .steps tr:nth-child(even) td{background:var(--row-alt)}
  .steps td.mark{text-align:center;padding:0}
  .steps td.mark svg{width:13px;height:13px;vertical-align:middle}

  .footer{position:absolute;left:0;top:776px;width:1200px;height:68px;
    background:linear-gradient(90deg,var(--green-1),var(--green-2));display:flex;align-items:center;padding-left:116px;color:#fff}
  .footer .site{font-size:24px;font-weight:700}
  .footer .rule{width:1px;height:30px;background:#fff;margin:0 18px}
  .footer .tagline{font-size:20px}
</style>
</head>
<body>
<svg width="0" height="0" style="position:absolute">
  <defs>
    <symbol id="tick" viewBox="0 0 16 16"><path d="M2 8.5l4 4 8-9" fill="none" stroke="#5cb82e" stroke-width="1.8" stroke-linecap="round" stroke-linejoin="round"/></symbol>
    <symbol id="cross" viewBox="0 0 16 16"><path d="M3.5 3.5l9 9M12.5 3.5l-9 9" fill="none" stroke="#e3131b" stroke-width="2.2" stroke-linecap="round"/></symbol>
  </defs>
</svg>

<div class="top-band"></div>
<div class="brand">Brelvona</div>
<div class="header-divider"></div>
<p class="notice">Unterlagen müssen gestellt werden, ansonsten werden Sie 1:1<br>verrechnet: GB-Auszug,GVZ, Nebenkostenabrechnung, STWEG-Protokolle<br>der letzten 3 Jahren, …</p>

<table class="packages">
  <colgroup><col class="task"><col class="basis"><col class="medium"><col class="sorglos"></colgroup>
  <thead>
    <tr class="package-head">
      <th class="blank"></th>
      <th class="basis">Basis-Paket</th>
      <th class="medium">Medium-Paket</th>
      <th class="sorglos">Sorglos</th>
    </tr>
    <tr class="price-row">
      <td class="section-title">Verkaufsablauf</td>
      <td>8'500.- CHF exkl. MWST</td>
      <td>10'900 CHF exkl. MWST</td>
      <td class="price-note">2% vom Verkaufspreis inkl. MWST (von<br>Grundstückgewinnsteuer abziehbar)</td>
    </tr>
  </thead>
  <tbody class="steps">
    <tr><td>Begehung Verkaufsobjekt</td><td class="mark"><svg><use href="#tick"/></svg></td><td class="mark"><svg><use href="#tick"/></svg></td><td class="mark"><svg><use href="#tick"/></svg></td></tr>
    <tr><td>Hedonische Schätzung intern &amp; Bank</td><td class="mark"><svg><use href="#tick"/></svg></td><td class="mark"><svg><use href="#tick"/></svg></td><td class="mark"><svg><use href="#tick"/></svg></td></tr>
    <tr><td>Marketing &amp; Vertriebskonzept</td><td class="mark"><svg><use href="#tick"/></svg></td><td class="mark"><svg><use href="#tick"/></svg></td><td class="mark"><svg><use href="#tick"/></svg></td></tr>
    <tr><td>Unterlagen einfordern- STWEG Protokolle, GB Auszug u.s.w wenn nötig</td><td class="mark"><svg><use href="#tick"/></svg></td><td class="mark"><svg><use href="#tick"/></svg></td><td class="mark"><svg><use href="#tick"/></svg></td></tr>
    <tr><td>Fotografieren &amp; Ausmessen der Immobilie</td><td class="mark"><svg><use href="#tick"/></svg></td><td class="mark"><svg><use href="#tick"/></svg></td><td class="mark"><svg><use href="#tick"/></svg></td></tr>
    <tr><td>Grundriss zeichnen</td><td class="mark"><svg><use href="#tick"/></svg></td><td class="mark"><svg><use href="#tick"/></svg></td><td class="mark"><svg><use href="#tick"/></svg></td></tr>
    <tr><td>Dokumentation erstellen</td><td class="mark"><svg><use href="#tick"/></svg></td><td class="mark"><svg><use href="#tick"/></svg></td><td class="mark"><svg><use href="#tick"/></svg></td></tr>
    <tr><td>Unsere Interessenten anschreiben</td><td class="mark"><svg><use href="#cross"/></svg></td><td class="mark"><svg><use href="#tick"/></svg></td><td class="mark"><svg><use href="#tick"/></svg></td></tr>
    <tr><td>Immobilie Online aufbereiten &amp; Aufschalten</td><td class="mark"><svg><use href="#tick"/></svg></td><td class="mark"><svg><use href="#tick"/></svg></td><td class="mark"><svg><use href="#tick"/></svg></td></tr>
    <tr><td>Anfragen beantworten- telefonisch &amp; elektronisch</td><td class="mark"><svg><use href="#cross"/></svg></td><td class="mark"><svg><use href="#tick"/></svg></td><td class="mark"><svg><use href="#tick"/></svg></td></tr>
    <tr><td>Besichtigungen koordinieren</td><td class="mark"><svg><use href="#cross"/></svg></td><td class="mark"><svg><use href="#cross"/></svg></td><td class="mark"><svg><use href="#tick"/></svg></td></tr>
    <tr><td>Besichtigungen Durchführen</td><td class="mark"><svg><use href="#cross"/></svg></td><td class="mark"><svg><use href="#cross"/></svg></td><td class="mark"><svg><use href="#tick"/></svg></td></tr>
    <tr><td>Interessenten &amp; Kaufangebote prüfen</td><td class="mark"><svg><use href="#cross"/></svg></td><td class="mark"><svg><use href="#tick"/></svg></td><td class="mark"><svg><use href="#tick"/></svg></td></tr>
    <tr><td>Evt. Bieterverfahren modern oder altmodisch</td><td class="mark"><svg><use href="#cross"/></svg></td><td class="mark"><svg><use href="#tick"/></svg></td><td class="mark"><svg><use href="#tick"/></svg></td></tr>
    <tr><td>Käufer zusage- andere noch vertrösten</td><td class="mark"><svg><use href="#cross"/></svg></td><td class="mark"><svg><use href="#tick"/></svg></td><td class="mark"><svg><use href="#tick"/></svg></td></tr>
    <tr><td>Sicherheitsnachweis (SINA)- organisieren</td><td class="mark"><svg><use href="#cross"/></svg></td><td class="mark"><svg><use href="#cross"/></svg></td><td class="mark"><svg><use href="#tick"/></svg></td></tr>
    <tr><td>Erstellung erster Kaufvertragsentwurf</td><td class="mark"><svg><use href="#tick"/></svg></td><td class="mark"><svg><use href="#tick"/></svg></td><td class="mark"><svg><use href="#tick"/></svg></td></tr>
    <tr><td>Berechnung provisorische Grundstückgewinnsteuer - Steueramt</td><td class="mark"><svg><use href="#cross"/></svg></td><td class="mark"><svg><use href="#cross"/></svg></td><td class="mark"><svg><use href="#tick"/></svg></td></tr>
    <tr><td>Beurkundungstermin vereinbaren</td><td class="mark"><svg><use href="#cross"/></svg></td><td class="mark"><svg><use href="#cross"/></svg></td><td class="mark"><svg><use href="#tick"/></svg></td></tr>
    <tr><td>Begleitung aufs Notariat</td><td class="mark"><svg><use href="#cross"/></svg></td><td class="mark"><svg><use href="#tick"/></svg></td><td class="mark"><svg><use href="#tick"/></svg></td></tr>
    <tr><td>Eigentumsübertragung vereinbaren</td><td class="mark"><svg><use href="#cross"/></svg></td><td class="mark"><svg><use href="#cross"/></svg></td><td class="mark"><svg><use href="#tick"/></svg></td></tr>
    <tr><td>Helfen bei der Steuererklärung für die definitive Grundstückgewinnsteuer</td><td class="mark"><svg><use href="#cross"/></svg></td><td class="mark"><svg><use href="#cross"/></svg></td><td class="mark"><svg><use href="#tick"/></svg></td></tr>
  </tbody>
</table>

<footer class="footer">
  <span class="site">brelvona.ch</span>
  <span class="rule"></span>
  <span class="tagline">Persönlich und Präzise</span>
</footer>
</body>
</html>
```